Still Brook Trail - Business Card

May try various combos of colors from primary & secondary palette attached below. Logo and Catch phrase previous built logo attached should go on front, but change to color palette options noted. may try various color options from minimal to zen like quality/vibe.
On Front: Attached Logo & Phrase
On Back:
https://stillbrooktrail.com/
415.283.7904
stillbrooktrail@openlanterndesk.ai

Contact Information for Business Card

Daniel R. Forsyth, MD Founder & CEO https://stillbrooktrail.com/ 415.283.7904 stillbrooktrail@openlanterndesk.ai

```html
<!DOCTYPE html>
<html lang="en">
<head>
<meta charset="utf-8">
<title>Still Brook Trail – Business Card</title>
<link rel="stylesheet" href="https://fonts.googleapis.com/css2?family=Arimo:wght@400;500&family=Exo+2:ital,wght@1,800&family=Montserrat:wght@400&family=Tinos&display=swap">
<style>
  :root {
    --page: #ebebeb;
    --forest: #3e5428;
    --paper: #ffffff;
    --chip: #7d8e68;
    --sage: #a3ad92;
  }
  * { box-sizing: border-box; margin: 0; padding: 0; }
  html, body { width: 1200px; height: 1200px; overflow: hidden; }
  body { background: var(--page); position: relative; font-family: "Arimo", Arial, sans-serif; }

  .card {
    position: absolute;
    left: 233px;
    width: 730px;
    height: 416px;
    border-radius: 35px;
    overflow: hidden;
  }
  .card--front { top: 150px; background: var(--paper); }
  .card--back  { top: 651px; background: var(--forest); }

  .front-panels { position: absolute; inset: 0; }

  .brand-seal {
    position: absolute;
    left: 45px; top: 103px;
    width: 238px; height: 238px;
    border: 2.5px solid var(--forest);
    border-radius: 50%;
    display: flex; align-items: center; justify-content: center;
  }
  .brand-seal__name {
    font-family: "Tinos", "Times New Roman", serif;
    font-weight: 400;
    color: var(--forest);
    font-size: 30px;
    line-height: 1.15;
    text-align: center;
  }

  .holder { position: absolute; left: 366px; top: 90px; color: var(--paper); }
  .holder__name {
    font-family: "Exo 2", sans-serif;
    font-style: italic; font-weight: 800;
    font-size: 30px; letter-spacing: -0.5px; line-height: 1;
  }
  .holder__role { font-size: 16px; font-weight: 500; margin-top: 4px; }

  .contacts { position: absolute; left: 368px; top: 277px; list-style: none; color: var(--paper); }
  .contacts::before {
    content: ""; position: absolute; left: 0; top: -4px;
    width: 29px; height: 112px; border-radius: 5px; background: var(--chip);
  }
  .contacts__item {
    position: relative; height: 28.3px;
    display: flex; align-items: center;
    font-size: 17px; letter-spacing: 0.1px;
  }
  .contacts__icon { width: 29px; display: flex; justify-content: center; margin-right: 13px; }
  .contacts__icon svg { width: 13px; height: 13px; }

  .back-seal {
    position: absolute; left: 302px; top: 103px;
    width: 126px; height: 126px;
    border: 2px solid var(--paper); border-radius: 50%;
  }
  .back-name {
    position: absolute; left: 0; right: 0; top: 248px; text-align: center;
    font-family: "Tinos", "Times New Roman", serif;
    font-weight: 400;
    color: var(--paper); font-size: 52px; line-height: 1;
  }
  .back-tagline {
    position: absolute; left: 0; right: 0; top: 310px; text-align: center;
    font-family: "Montserrat", sans-serif;
    color: var(--sage); font-size: 20px;
  }
</style>
</head>
<body>

<section class="card card--front">
  <svg class="front-panels" width="730" height="416" viewBox="0 0 730 416">
    <path fill="var(--forest)" d="M278 0 L730 0 L730 180 L402 180 Q376 180 364 160 Z"/>
    <path fill="var(--forest)" d="M730 192 L412 192 Q390 192 378 216 L288 416 L730 416 Z"/>
  </svg>

  <div class="brand-seal">
    <p class="brand-seal__name">Still Brook<br>Trail</p>
  </div>

  <div class="holder">
    <h1 class="holder__name">MY NAME</h1>
    <p class="holder__role">Founder &amp; Director</p>
  </div>

  <ul class="contacts">
    <li class="contacts__item">
      <span class="contacts__icon"><svg viewBox="0 0 16 16"><path fill="#fff" d="M4 1.5l2.3 3-1.4 1.6a9 9 0 0 0 5 5l1.6-1.4 3 2.3-1.6 2.3C7.6 14.3 1.7 8.4 1.7 3.1z"/></svg></span>
      415 283 7904
    </li>
    <li class="contacts__item">
      <span class="contacts__icon"><svg viewBox="0 0 16 16"><rect x="4" y="1" width="8" height="14" rx="1.5" fill="none" stroke="#fff" stroke-width="1.6"/></svg></span>
      000 000 0000
    </li>
    <li class="contacts__item">
      <span class="contacts__icon"><svg viewBox="0 0 16 16"><rect x="1" y="3.5" width="14" height="9.5" rx="1" fill="#fff"/><path d="M1.5 4l6.5 5 6.5-5" fill="none" stroke="var(--chip)" stroke-width="1.3"/></svg></span>
      stillbrooktrail@openlanterndesk.ai
    </li>
    <li class="contacts__item">
      <span class="contacts__icon"><svg viewBox="0 0 16 16"><g fill="none" stroke="#fff" stroke-width="1.3"><circle cx="8" cy="8" r="6.5"/><ellipse cx="8" cy="8" rx="2.8" ry="6.5"/><path d="M1.5 8h13M2.5 4.8h11M2.5 11.2h11"/></g></svg></span>
      https://stillbrooktrail.com/
    </li>
  </ul>
</section>

<section class="card card--back">
  <div class="back-seal"></div>
  <h2 class="back-name">Still Brook Trail</h2>
  <p class="back-tagline">Nurturing Steady Hearts, Minds &amp; Souls</p>
</section>

</body>
</html>
```